Logo, homepage, and product page design cleaning equipment

Looking for a logo, homepage, and product page design for our cartwell store. We sell cleaning equipment that serves the auto detailing industry. I have attached a picture of our main product. The company is called Brisk Cleaning Equipment with a slogan of The Way to Clean (slogan incorporated is optional). A site I really like is https://www.harborlanternroast.example/. It has a very clean layout and very clear on their messaging.

Target Market(s)

Auto detailing industry

Industry/Entity Type

Automotive

Logo Text

Brisk Cleaning Equipment

Font styles to use
Serif
Sans Serif

Requirements
Must have
• A nice clean layout. Not too busy. Easy to navigate.
Nice to have
• consistency in colors. Appeal to people who care about their cars. They have an eye for detail.
Should not have
• It cannot be too busy.

```html
<!DOCTYPE html>
<html lang="en">
<head>
<meta charset="utf-8">
<title>Brisk Cleaning Equipment</title>
<link href="https://fonts.googleapis.com/css2?family=Raleway:wght@500;600;700;800&family=Open+Sans:ital,wght@0,400;0,600;0,700;1,400&display=swap" rel="stylesheet">
<style>
:root{
  --ink:#1b1b1b;
  --text:#555;
  --muted:#8a8a8a;
  --blue:#2d7dc3;
  --blue-dark:#2469a6;
  --topbar:#1e1e1e;
  --light:#f1f1f1;
  --line:#e2e2e2;
  --white:#fff;
}
*{box-sizing:border-box;margin:0;padding:0}
html,body{width:1200px;height:5158px;overflow:hidden;background:var(--white)}
body{font-family:"Open Sans",Arial,sans-serif;color:var(--text);position:relative}
.h{font-family:"Raleway",Arial,sans-serif;color:var(--ink);font-weight:700;text-transform:uppercase}
.abs{position:absolute}
.ph{position:absolute}

.topbar{top:0;left:0;width:1200px;height:38px;background:var(--topbar);color:#fff;font-size:13px;letter-spacing:.5px;text-align:center;line-height:38px;text-transform:uppercase}
.social{display:flex;gap:9px}
.social span{width:30px;height:30px;border:1px solid var(--blue);border-radius:50%;display:block}
.header-social{top:80px;left:100px}
.logo{top:66px;left:0;width:1200px;text-align:center;font-size:24px;line-height:32px;letter-spacing:.5px}
.header-icons{top:90px;right:100px;display:flex;gap:22px}
.nav{top:160px;left:0;width:1200px;height:46px;border-bottom:1px solid var(--line);display:flex;justify-content:center;gap:60px;font-size:14px;font-weight:600;color:var(--ink);text-transform:uppercase;line-height:36px}

.hero{top:206px;left:0;width:1200px;height:523px;background:linear-gradient(90deg,#f3f3f3,#e9e9e9)}
.hero-title{top:140px;left:100px;font-size:46px;line-height:56px;font-weight:700}
.hero-title b{font-size:66px;font-weight:700;display:block;line-height:78px}
.btn{background:var(--blue);color:#fff;font-family:"Raleway",Arial,sans-serif;font-weight:700;font-size:14px;text-transform:uppercase;border-radius:30px;text-align:center}
.hero-btn{top:300px;left:100px;width:170px;height:52px;line-height:52px}
.hero-product{top:30px;left:510px;width:640px;height:493px;background:radial-gradient(ellipse at 40% 55%,#2a2a2a 0 38%,rgba(0,0,0,0) 39%)}

.welcome-title{top:805px;left:0;width:1200px;text-align:center;font-size:34px}
.welcome-text{top:875px;left:300px;width:600px;text-align:center;font-size:13px;line-height:21px}
.divider{left:100px;width:1000px;height:1px;background:var(--line)}

.section-title{left:0;width:1200px;text-align:center;font-size:32px}
.tile{top:1183px;width:316px;height:330px}

.video{top:1719px;left:0;width:1200px;height:433px;background:linear-gradient(100deg,#0c0c0c 0%,#2a2a2a 45%,#cfd3d6 55%,#222 75%,#111 100%)}
.play{top:1900px;left:565px}

.product-img{top:2266px;left:100px;width:433px;height:436px;background:radial-gradient(ellipse at 50% 55%,#222 0 35%,#f2f2f2 36%)}
.product-title{top:2312px;left:560px;width:540px;text-align:center;font-size:32px}
.price{top:2376px;left:560px;width:540px;text-align:center;font-size:28px;font-weight:700;color:var(--blue);font-family:"Raleway",Arial,sans-serif}
.share{top:2440px;left:560px;width:540px;display:flex;justify-content:center;gap:12px}
.share span{background:var(--blue);color:#fff;font-size:11px;font-weight:700;padding:2px 10px;border-radius:3px}
.share span.s2{background:#c23030}
.qty{top:2508px;left:560px;width:540px;display:flex;justify-content:center;align-items:center;gap:22px;font-size:14px}
.qty span.box{width:62px;height:40px;border:1px solid #ccc;text-align:center;line-height:40px;color:var(--ink)}
.cart-btn{top:2596px;left:780px;width:152px;height:50px;line-height:50px}

.split-text{width:600px;height:416px;background:var(--light);padding:80px 100px 0 100px}
.split-text h3{font-size:34px;line-height:42px;margin-bottom:26px}
.split-text p{font-size:13px;line-height:24px}

.post{top:3835px;width:237px}
.post .date{font-size:12px;color:var(--muted)}
.post h4{font-family:"Raleway",Arial,sans-serif;font-size:20px;font-weight:700;color:var(--ink);margin:6px 0 10px}
.post .thumb{width:237px;height:165px}
.post p{font-size:12.5px;line-height:20px;margin-top:30px}

.quote{top:4284px;left:0;width:1200px;height:399px;background:var(--blue);color:#fff;text-align:center;padding:68px 250px 0}
.quote p{font-style:italic;font-size:15px;line-height:27px}
.quote .who{font-family:"Raleway",Arial,sans-serif;font-weight:700;font-size:18px;margin-top:36px;font-style:normal}

.foot-logo{top:4735px;left:100px;font-size:28px;line-height:36px}
.foot-text{top:4830px;left:100px;width:340px;font-size:12.5px;line-height:20px}
.foot-head{font-size:16px}
.follow{top:4750px;left:500px}
.follow .social{margin-top:34px;gap:14px}
.follow .social span{width:42px;height:42px}
.news{top:4750px;left:800px}
.news .row{display:flex;margin-top:34px}
.news .field{width:220px;height:44px;border:1px solid #ccc;font-size:13px;line-height:44px;padding-left:14px;color:var(--muted)}
.news .send{width:82px;height:44px;background:var(--blue);color:#fff;font-weight:700;font-size:13px;text-align:center;line-height:44px;text-transform:uppercase;font-family:"Raleway",Arial,sans-serif}
.cards{top:5030px;left:0;width:1200px;display:flex;justify-content:center;gap:8px}
.cards span{width:58px;height:36px;border-radius:3px;background:#d8d8d8}
.copyright{top:5094px;left:0;width:1200px;text-align:center;font-size:12px}
</style>
</head>
<body>

<div class="abs topbar">Free shipping for domestic orders over $50!</div>

<div class="abs social header-social"><span></span><span></span><span></span><span></span></div>
<div class="abs logo h">Brisk Cleaning<br>Equipment</div>
<div class="abs header-icons">
  <svg width="20" height="20" viewBox="0 0 20 20"><circle cx="8" cy="8" r="6" fill="none" stroke="#222" stroke-width="2.2"/><line x1="12.5" y1="12.5" x2="18" y2="18" stroke="#222" stroke-width="2.4"/></svg>
  <svg width="22" height="20" viewBox="0 0 22 20"><path d="M1 2h4l3 11h11l2-8H7" fill="none" stroke="#222" stroke-width="2"/><circle cx="9" cy="17" r="1.8" fill="#222"/><circle cx="17" cy="17" r="1.8" fill="#222"/></svg>
</div>
<nav class="abs nav"><span>Home</span><span>Product</span><span>Shop</span><span>Contact</span><span>FAQ</span><span>About</span></nav>

<section class="abs hero">
  <div class="ph hero-product" role="img" aria-label="Black foam pressure sprayer with blue cap, product shot"></div>
  <h1 class="abs hero-title h">The way<b>to clean</b></h1>
  <div class="abs btn hero-btn">Shop now!</div>
</section>

<h2 class="abs welcome-title h">Welcome to Brisk Cleaning Equipment</h2>
<p class="abs welcome-text">Nemo enim ipsam voluptatem quia voluptas sit aspernatur aut odit aut fugit, sed quia consequuntur magni dolores eos qui ratione voluptatem sequi nesciunt. Neque porro quisquam est, qui dolorem ipsum quia dolor sit amet, consectetur, adipisci velit, sed quia non numquam eius modi tempora incidunt ut labore et dolore magnam aliquam quaerat voluptatem. Ut enim ad minima veniam, quis nostrum.</p>
<div class="abs divider" style="top:1031px"></div>

<h2 class="abs section-title h" style="top:1090px">Product that fit your life</h2>
<div class="ph tile" style="left:100px;background:linear-gradient(135deg,#cfd8de,#8a97a3)" role="img" aria-label="Smiling woman spraying a car window"></div>
<div class="ph tile" style="left:440px;background:linear-gradient(160deg,#e8d27a,#1c1c1c 55%)" role="img" aria-label="Yellow sponge on a wet black car surface"></div>
<div class="ph tile" style="left:784px;background:linear-gradient(135deg,#2e5fae,#c8382a 60%,#e07a2a)" role="img" aria-label="Detailer wiping a red car with an orange cloth"></div>

<div class="ph video" role="img" aria-label="Video still of foam sprayed onto a car wheel"></div>
<svg class="abs play" width="70" height="70" viewBox="0 0 70 70"><circle cx="35" cy="35" r="32" fill="none" stroke="#fff" stroke-width="3"/><path d="M28 22l20 13-20 13z" fill="#fff"/></svg>

<div class="ph product-img" role="img" aria-label="Black foam sprayer with blue cap on white"></div>
<h2 class="abs product-title h">Brisk Cleaning Equipment</h2>
<div class="abs price">$80.00</div>
<div class="abs share"><span>Share</span><span class="s2">Save</span><span>Like</span></div>
<div class="abs qty"><span>Quantity</span><span class="box">1</span></div>
<div class="abs btn cart-btn">Add to cart</div>

<div class="abs split-text" style="top:2819px;left:0">
  <h3 class="h">Auto detailing<br>industry</h3>
  <p>Nam libero tempore, cum soluta nobis est eligendi optio cumque nihil impedit quo minus id quod maxime placeat facere possimus, omnis voluptas assumenda est, omnis dolor repellendus. Temporibus autem quibusdam et aut officiis debitis aut rerum necessitatibus saepe eveniet ut et voluptates repudiandae sint et molestiae.</p>
</div>
<div class="ph" style="top:2819px;left:600px;width:600px;height:416px;background:linear-gradient(180deg,#1c1c1c 0%,#2b2b2b 70%,#e4e4e4 71%)" role="img" aria-label="Close-up of the sprayer bottle base"></div>
<div class="ph" style="top:3235px;left:0;width:600px;height:416px;background:linear-gradient(135deg,#1d4f8a,#6f98c4 55%,#d7e3ee)" role="img" aria-label="Hand washing a blue car with foam"></div>
<div class="abs split-text" style="top:3235px;left:600px">
  <h3 class="h">Finibus bonorum<br>et maloru</h3>
  <p>Nam libero tempore, cum soluta nobis est eligendi optio cumque nihil impedit quo minus id quod maxime placeat facere possimus, omnis voluptas assumenda est, omnis dolor repellendus. Temporibus autem quibusdam et aut officiis debitis aut rerum necessitatibus saepe eveniet ut et voluptates repudiandae sint et molestiae.</p>
</div>

<h2 class="abs section-title h" style="top:3748px">Our blog</h2>
<article class="abs post" style="left:100px"><div class="date">&#9633; May 20, 2018</div><h4>Bonorumet Maloru</h4><div class="thumb" style="background:linear-gradient(135deg,#3a3f45,#4aa3c8)" role="img" aria-label="Blue mitt washing a car"></div><p>Nam libero tempore, cum soluta nobis est eligendi optio cumque nihil impedit quo minus id quod maxime placeat facere possimus nis volu.</p></article>
<article class="abs post" style="left:354px"><div class="date">&#9633; May 20, 2018</div><h4>Bonorumet Maloru</h4><div class="thumb" style="background:linear-gradient(135deg,#222,#8c8c8c 60%,#c9c9c9)" role="img" aria-label="Car wheel being cleaned with a brush"></div><p>Nam libero tempore, cum soluta nobis est eligendi optio cumque nihil impedit quo minus id quod maxime placeat facere possimus nis volu.</p></article>
<article class="abs post" style="left:608px"><div class="date">&#9633; May 20, 2018</div><h4>Bonorumet Maloru</h4><div class="thumb" style="background:linear-gradient(160deg,#6fa7d6,#d9e6ef 50%,#3a3a3a)" role="img" aria-label="Car wash bay under a blue sky"></div><p>Nam libero tempore, cum soluta nobis est eligendi optio cumque nihil impedit quo minus id quod maxime placeat facere possimus nis volu.</p></article>
<article class="abs post" style="left:863px"><div class="date">&#9633; May 20, 2018</div><h4>Bonorumet Maloru</h4><div class="thumb" style="background:linear-gradient(135deg,#2b2b2b,#c7302a 50%,#e2b62c)" role="img" aria-label="Colourful detailing brushes on a wheel"></div><p>Nam libero tempore, cum soluta nobis est eligendi optio cumque nihil impedit quo minus id quod maxime placeat facere possimus nis volu.</p></article>

<section class="abs quote">
  <p>&ldquo; At vero eos et accusamus et iusto odio dignissimos ducimus qui blanditiis praesentium voluptatum deleniti atque corrupti quos dolores et quas molestias excepturi sint occaecati cupiditate non provident, similique sunt in culpa qui officia deserunt mollitia animi, id est laborum et dolorum fuga. Et harum quidem rerum facilis est et expedita distinctio. Nam libero tempore, cum soluta nobis est eligendi optio cumque nihil impedit quo minus id quod maxime placeat facere possimus.&rdquo;</p>
  <div class="who">- JOHN DOE</div>
</section>

<div class="abs foot-logo h">Brisk Cleaning<br>Equipment</div>
<p class="abs foot-text">Itaque earum rerum hic tenetur a sapiente delectus, ut aut reiciendis voluptatibus maiores alias consequatur aut perferendis doloribus asperiores repellat quasi totem sequi nesci e porro quisqua.</p>
<div class="abs follow"><div class="foot-head h">Follow us out there</div><div class="social"><span></span><span></span><span></span><span></span></div></div>
<div class="abs news"><div class="foot-head h">Newsletter sign up</div><div class="row"><div class="field">Email Address</div><div class="send">Submit</div></div></div>
<div class="abs divider" style="top:4975px"></div>
<div class="abs cards"><span></span><span></span><span></span><span></span><span></span></div>
<div class="abs copyright">Copyright &copy; 2018, Brisk Cleaning Equipment. All Rights Reserved.</div>

</body>
</html>
```